Heal the world with your creativity.

We're looking for advertising materials (social media, email, etc) for a new mental health platform called PIM (www.seepim.example). PIM’s mission is to empower our members to heal and thrive by making expert advice and real-life experiences accessible to all.

Note

Facebook Cover Images: 820 x 312 pixels
LinkedIn Cover Images: 1128 x 191 pixels
3 x Social Media Post Image Templates: 1080 x 1080 pixles
3 x Enewsletter Header Image Templates: 1080 x 360 pixels
Sales One sheet: US Letter (8.5 x 11 inches)
Overview Powerpoint template: 13.33 x 7.5 inches

Fonts to Use:
Galanogrotesque
Montserrat regular

Target Market(s)

18 - 35 year olds

Industry/Entity Type

Mental Health

Requirements
Must have
• Facebook Cover Images: 820 x 312 pixels
3 x Enewsletter Header Images: 1080 x 360 pixels

Fonts to Use:
Galanogrotesque
Montserrat regular
Nice to have
• Creative copywriting for social media posts

```html
<!DOCTYPE html>
<html lang="en">
<head>
<meta charset="utf-8">
<title>PIM Mission Banner Set</title>
<link rel="stylesheet" href="https://fonts.googleapis.com/css2?family=Montserrat:wght@400;600&family=Red+Hat+Display:wght@800&display=swap">
<style>
  :root {
    --orange: #f07c33;
    --sky: #a8cbde;
    --mist: #c3d5dd;
    --steel: #3d7297;
    --denim: #336a91;
    --navy: #0b4068;
    --teal: #4d877e;
    --ink: #23384d;
    --white: #ffffff;
    --page: #ffffff;
  }
  html, body { margin: 0; padding: 0; overflow: hidden; }
  body { width: 1200px; height: 1200px; background: var(--page); position: relative; }
  .banner { position: absolute; display: block; box-shadow: 2px 3px 3px rgba(0,0,0,0.35); }
  .banner--facebook { left: 100px; top: 74px; width: 492px; height: 187px; }
  .banner--linkedin { left: 637px; top: 124px; width: 521px; height: 89px; }
  .banner--post { left: 100px; top: 285px; width: 521px; height: 520px; }
  .banner--header { left: 652px; top: 366px; width: 491px; height: 163px; }
  .banner--newsletter { left: 100px; top: 827px; width: 521px; height: 293px; }
  .banner--portrait { left: 697px; top: 607px; width: 403px; height: 521px; }
  .heading { font-family: "Red Hat Display", "Montserrat", sans-serif; font-weight: 800; letter-spacing: 0.5px; }
  .body-copy { font-family: "Montserrat", sans-serif; font-weight: 400; }
  .brand-name { font-family: "Montserrat", sans-serif; font-weight: 600; fill: var(--white); }
  .photo-warm { fill: url(#warm); }
</style>
</head>
<body>

<svg width="0" height="0" style="position:absolute">
  <defs>
    <linearGradient id="warm" x1="0" y1="0" x2="1" y2="1">
      <stop offset="0" stop-color="#c9925a"/>
      <stop offset="0.55" stop-color="#a9744a"/>
      <stop offset="1" stop-color="#6e4a33"/>
    </linearGradient>
    <linearGradient id="tealPhoto" x1="0" y1="0" x2="1" y2="1">
      <stop offset="0" stop-color="#5b9a8f"/>
      <stop offset="1" stop-color="#3f7a72"/>
    </linearGradient>
    <linearGradient id="street" x1="0" y1="0" x2="1" y2="0">
      <stop offset="0" stop-color="#8a7460"/>
      <stop offset="1" stop-color="#5d534b"/>
    </linearGradient>
    <linearGradient id="garden" x1="0" y1="0" x2="1" y2="1">
      <stop offset="0" stop-color="#4d5b40"/>
      <stop offset="1" stop-color="#8a7a6a"/>
    </linearGradient>
  </defs>
</svg>

<!-- Facebook cover -->
<svg class="banner banner--facebook" viewBox="0 0 787 298">
  <defs><clipPath id="c1"><rect width="787" height="298"/></clipPath></defs>
  <g clip-path="url(#c1)">
    <rect width="787" height="298" fill="var(--orange)"/>
    <path d="M580,0 Q430,150 410,298 L787,298 L787,0 Z" fill="url(#tealPhoto)" role="img" aria-label="Teal-tinted photo of young friends"/>
    <circle cx="140" cy="115" r="180" fill="var(--mist)"/>
    <circle cx="490" cy="150" r="125" class="photo-warm" stroke="var(--white)" stroke-width="4" role="img" aria-label="Photo of two friends hugging"/>
    <circle cx="665" cy="213" r="85" fill="url(#garden)" stroke="var(--white)" stroke-width="4" role="img" aria-label="Photo of a smiling young woman"/>
    <circle cx="710" cy="68" r="50" fill="var(--orange)"/>
    <text x="710" y="78" text-anchor="middle" font-size="30" class="brand-name">PIM</text>
    <text x="40" y="68" font-size="27" fill="var(--navy)" class="heading">PIM’S MISSION</text>
    <g class="body-copy" font-size="23" fill="var(--ink)">
      <text x="40" y="107">To empower our</text>
      <text x="40" y="134">members to heal</text>
      <text x="40" y="161">and thrive by making</text>
      <text x="40" y="188">expert advice and</text>
      <text x="40" y="215">real-life experiences</text>
      <text x="40" y="242">accessible to all.</text>
    </g>
  </g>
</svg>

<!-- LinkedIn cover -->
<svg class="banner banner--linkedin" viewBox="0 0 833 142">
  <defs><clipPath id="c2"><rect width="833" height="142"/></clipPath></defs>
  <g clip-path="url(#c2)">
    <rect width="833" height="142" fill="#3a6d93"/>
    <circle cx="20" cy="20" r="210" fill="var(--sky)"/>
    <rect x="680" y="0" width="153" height="142" fill="var(--orange)"/>
    <path d="M555,142 Q560,10 690,8 Q790,6 833,100 V142 Z" fill="url(#street)" role="img" aria-label="Photo of three friends walking in the city"/>
    <circle cx="85" cy="73" r="48" fill="var(--orange)"/>
    <text x="85" y="83" text-anchor="middle" font-size="29" class="brand-name">PIM</text>
    <text x="388" y="50" text-anchor="middle" font-size="22" fill="var(--white)" class="heading">PIM’S MISSION</text>
    <g class="body-copy" font-size="12.5" fill="var(--white)" text-anchor="middle">
      <text x="388" y="76">To empower our members to heal and</text>
      <text x="388" y="91">thrive by making expert advice and real-life</text>
      <text x="388" y="106">experiences accessible to all.</text>
    </g>
  </g>
</svg>

<!-- Social post -->
<svg class="banner banner--post" viewBox="0 0 833 832">
  <defs><clipPath id="c3"><rect width="833" height="832"/></clipPath></defs>
  <g clip-path="url(#c3)">
    <rect width="833" height="832" fill="var(--sky)"/>
    <circle cx="460" cy="160" r="300" fill="var(--denim)"/>
    <ellipse cx="90" cy="380" rx="420" ry="410" class="photo-warm" role="img" aria-label="Photo of a young woman outdoors in autumn light"/>
    <circle cx="830" cy="1160" r="790" fill="var(--steel)"/>
    <circle cx="700" cy="190" r="82" fill="var(--orange)"/>
    <text x="700" y="205" text-anchor="middle" font-size="46" class="brand-name">PIM</text>
    <text x="780" y="587" text-anchor="end" font-size="37" fill="var(--white)" class="heading">PIM’S MISSION</text>
    <g class="body-copy" font-size="29" fill="var(--white)" text-anchor="end">
      <text x="778" y="643">To empower our members</text>
      <text x="778" y="677">to heal and thrive by making</text>
      <text x="778" y="711">expert advice and real-life</text>
      <text x="778" y="745">experiences accessible to all.</text>
    </g>
  </g>
</svg>

<!-- Email header -->
<svg class="banner banner--header" viewBox="0 0 785 261">
  <defs><clipPath id="c4"><rect width="785" height="261"/></clipPath></defs>
  <g clip-path="url(#c4)">
    <rect width="785" height="261" fill="var(--orange)"/>
    <circle cx="65" cy="60" r="120" fill="var(--navy)"/>
    <circle cx="260" cy="130" r="142" fill="var(--mist)"/>
    <circle cx="68" cy="65" r="50" fill="var(--orange)"/>
    <text x="68" y="75" text-anchor="middle" font-size="29" class="brand-name">PIM</text>
    <circle cx="650" cy="145" r="228" fill="var(--navy)"/>
    <circle cx="665" cy="150" r="210" fill="url(#garden)" stroke="var(--white)" stroke-width="4" role="img" aria-label="Photo of a laughing couple embracing"/>
    <text x="260" y="70" text-anchor="middle" font-size="23" fill="var(--navy)" class="heading">PIM’S MISSION</text>
    <g class="body-copy" font-size="19" fill="var(--ink)" text-anchor="middle">
      <text x="260" y="103">To empower our</text>
      <text x="260" y="126">members to heal</text>
      <text x="260" y="149">and thrive by making</text>
      <text x="260" y="172">expert advice and</text>
      <text x="260" y="195">real-life experiences</text>
      <text x="260" y="218">accessible to all.</text>
    </g>
  </g>
</svg>

<!-- Newsletter header -->
<svg class="banner banner--newsletter" viewBox="0 0 833 469">
  <defs><clipPath id="c5"><rect width="833" height="469"/></clipPath></defs>
  <g clip-path="url(#c5)">
    <rect width="833" height="469" fill="var(--sky)"/>
    <circle cx="270" cy="40" r="120" fill="var(--navy)"/>
    <circle cx="580" cy="100" r="275" fill="var(--orange)"/>
    <circle cx="590" cy="90" r="265" class="photo-warm" stroke="var(--white)" stroke-width="6" role="img" aria-label="Photo of two friends hugging"/>
    <circle cx="88" cy="113" r="55" fill="var(--orange)"/>
    <text x="88" y="124" text-anchor="middle" font-size="32" class="brand-name">PIM</text>
    <text x="34" y="300" font-size="29" fill="var(--navy)" class="heading">PIM’S MISSION</text>
    <g class="body-copy" font-size="20" fill="var(--ink)">
      <text x="34" y="335">To empower our members</text>
      <text x="34" y="358">to heal and thrive by making</text>
      <text x="34" y="381">expert advice and real-life</text>
      <text x="34" y="404">experiences accessible to all.</text>
    </g>
  </g>
</svg>

<!-- Portrait post -->
<svg class="banner banner--portrait" viewBox="0 0 644 833">
  <defs><clipPath id="c6"><rect width="644" height="833"/></clipPath></defs>
  <g clip-path="url(#c6)">
    <rect width="644" height="833" fill="var(--sky)"/>
    <circle cx="430" cy="130" r="420" class="photo-warm" stroke="var(--white)" stroke-width="6" role="img" aria-label="Photo of a couple holding hands"/>
    <circle cx="243" cy="560" r="225" fill="var(--navy)" stroke="var(--white)" stroke-width="8"/>
    <circle cx="532" cy="711" r="68" fill="var(--orange)"/>
    <text x="532" y="724" text-anchor="middle" font-size="38" class="brand-name">PIM</text>
    <text x="243" y="455" text-anchor="middle" font-size="35" fill="var(--white)" class="heading">PIM’S MISSION</text>
    <g class="body-copy" font-size="28" fill="var(--white)" text-anchor="middle">
      <text x="243" y="507">To empower our</text>
      <text x="243" y="541">members to heal</text>
      <text x="243" y="575">and thrive by making</text>
      <text x="243" y="609">expert advice and</text>
      <text x="243" y="643">real-life experiences</text>
      <text x="243" y="677">accessible to all.</text>
    </g>
  </g>
</svg>

</body>
</html>
```